Website Hero Image Redesign Brief
The current hero image appears too busy and lacks the elegance that reflects our brand. We would like to create a new, refined hero image for our real estate company's website.
Requirements:
Clean, elegant, and modern look
Should represent premium real estate sales
Use either our existing images from the website or create a custom design
Focus on sophistication, trust, and exclusivity
Ensure the image works well with overlay text and call-to-action buttons

Goal:
The new hero image should immediately convey professionalism, elegance, and the premium nature of our real estate services, while maintaining a calm and inviting visual impression.

Website: https://www.lindqvoltwohnen.example/

```html
<!DOCTYPE html>
<html lang="de">
<head>
<meta charset="utf-8">
<title>Lindqvolt Wohnen – Startseite</title>
<link rel="stylesheet" href="https://fonts.googleapis.com/css2?family=Montserrat:wght@500;600&family=Oswald:wght@500&family=Arimo&display=swap">
<style>
  :root {
    --backdrop: #333333;
    --hero-top: #0c3536;
    --hero-bottom: #123f1f;
    --panel-shade: rgba(0, 20, 18, 0.45);
    --brand-green: #3fae49;
    --text-light: #ffffff;
    --frame: #ffffff;
    --gap-green: #0a3a22;
  }
  * { box-sizing: border-box; margin: 0; padding: 0; }
  html, body { width: 1200px; height: 1001px; overflow: hidden; background: var(--backdrop); }
  .hero {
    position: absolute; left: 101px; top: 250px; width: 998px; height: 494px;
    overflow: hidden;
  }
  .hero-backdrop {
    position: absolute; inset: 0;
    background: linear-gradient(180deg, var(--hero-top) 0%, #0e3a2f 40%, var(--hero-bottom) 75%, #103a1c 100%);
  }
  .side-panel { position: absolute; left: 0; top: 0; width: 266px; height: 100%; background: var(--panel-shade); }
  .brand {
    position: absolute; left: 75px; top: 26px; width: 150px;
    font: 600 18px/20px "Montserrat", sans-serif; color: var(--brand-green);
  }
  .main-nav { position: absolute; left: 284px; top: 36px; display: flex; gap: 10px; }
  .main-nav a {
    font: 500 11px/1 "Oswald", sans-serif; letter-spacing: 0.3px;
    color: var(--text-light); text-decoration: none; padding-bottom: 7px;
  }
  .main-nav a.is-active { border-bottom: 2px solid var(--brand-green); }
  .headline {
    position: absolute; left: 74px; top: 228px;
    font: 500 42px/44px "Montserrat", sans-serif; color: var(--text-light); letter-spacing: 0.4px;
  }
  .tagline {
    position: absolute; left: 76px; top: 320px;
    font: 500 14.5px/1 "Montserrat", sans-serif; color: var(--brand-green);
  }
  .sales-title {
    position: absolute; right: 345px; top: 114px; text-align: right;
    font: 22px/28px "Arimo", sans-serif; color: var(--text-light);
  }
  .gap-block { position: absolute; left: 706px; top: 230px; width: 48px; height: 72px; background: var(--gap-green); }
  .sale-photo { position: absolute; border: 5px solid var(--frame); }
  .sale-photo.dining { left: 678px; top: 141px; width: 184px; height: 116px; background: linear-gradient(160deg, #f4f2ee 0%, #d9d2c6 55%, #6b4a2e 100%); }
  .sale-photo.living { left: 522px; top: 210px; width: 179px; height: 119px; background: linear-gradient(150deg, #e9e4da 0%, #cfc6b6 50%, #7a5a3e 100%); }
  .sale-photo.street { left: 657px; top: 306px; width: 184px; height: 116px; background: linear-gradient(180deg, #d8cfb8 0%, #7d8a5c 50%, #bdb6a8 100%); }
  .sale-photo.terrace { left: 754px; top: 206px; width: 183px; height: 120px; background: linear-gradient(180deg, #d9b472 0%, #e2c68c 25%, #5d87a8 45%, #4c6f3a 70%, #a6653f 100%); }
</style>
</head>
<body>
  <section class="hero">
    <div class="hero-backdrop" role="img" aria-label="Abgedunkeltes Foto eines Mehrfamilienhauses auf grüner Wiese vor bewaldetem Hügel"></div>
    <div class="side-panel"></div>

    <div class="brand">Lindqvolt<br>Wohnen</div>

    <nav class="main-nav">
      <a href="#" class="is-active">STARTSEITE</a>
      <a href="#">ÜBERUNS</a>
      <a href="#">VERKAUF</a>
      <a href="#">UNSERE</a>
      <a href="#">REFEREKZOBJEKTE</a>
      <a href="#">RÜCKRUF-SERVICE</a>
      <a href="#">KONTAKT</a>
    </nav>

    <h1 class="headline">Ihr lokaler<br>Immobilienprofi</h1>
    <p class="tagline">in Meilen verwurzelt - am Zürichsee unterwegs</p>

    <h2 class="sales-title">Eusi<br>erfolgrichi<br>Verkäuf</h2>

    <div class="gap-block"></div>
    <div class="sale-photo dining" role="img" aria-label="Helles Esszimmer mit Holztisch und offenem Wohnbereich"></div>
    <div class="sale-photo living" role="img" aria-label="Wohnzimmer mit weissem Ledersofa und Essbereich"></div>
    <div class="sale-photo street" role="img" aria-label="Wohnhaus mit Vorgarten an einer Strasse"></div>
    <div class="sale-photo terrace" role="img" aria-label="Terrasse mit Markise und Blick auf den See"></div>
  </section>
</body>
</html>
```